Business Card - Cooperate

Business Card for Larkfield Management Consulting

Target Market(s)

Corparte - b2B

Industry/Entity Type

Management Consulting - Professional Services

Contact Information for Business Card

Company Name , Slogan , Dummy Address,

Requirements
Must have
• Reach your Full Potential

```html
<!DOCTYPE html>
<html lang="en">
<head>
<meta charset="utf-8">
<title>Larkfield Management Consulting – Business Card</title>
<link rel="stylesheet" href="https://fonts.googleapis.com/css2?family=Montserrat:wght@400;500;600;700&display=swap">
<style>
  :root {
    --canvas: #d9d9d9;
    --card-white: #f4f4f4;
    --card-white-shade: #e9e9e9;
    --card-black: #050505;
    --brand-blue: #0d47c7;
    --brand-navy: #1f2a8c;
    --brand-green: #3cc33a;
    --brand-teal: #1fa58f;
    --text-dark: #1b1b1b;
    --white: #ffffff;
  }
  * { margin: 0; padding: 0; box-sizing: border-box; }
  html, body {
    width: 1084px; height: 1200px; overflow: hidden;
    background: var(--canvas);
    font-family: "Montserrat", sans-serif;
  }
  .canvas {
    position: relative; width: 1084px; height: 1200px;
    display: flex; justify-content: center; align-items: center; gap: 60px;
  }
  .card {
    position: relative; width: 420px; height: 748px; overflow: hidden;
    box-shadow: 0 10px 24px rgba(0,0,0,0.22);
  }
  /* Front */
  .card-front {
    background: linear-gradient(135deg, var(--white) 0%, var(--card-white) 55%, var(--card-white-shade) 100%);
    text-align: center; color: var(--text-dark);
  }
  .brand {
    position: absolute; top: 68px; left: 0; right: 0;
    display: flex; justify-content: center; align-items: center; gap: 14px;
  }
  .brand-dot {
    width: 34px; height: 34px; border-radius: 50%; background: var(--brand-blue);
  }
  .brand-name {
    font-weight: 600; font-size: 46px; letter-spacing: 1px; color: var(--brand-blue);
  }
  .person { position: absolute; top: 276px; left: 0; right: 0; }
  .person-name { font-weight: 600; font-size: 31px; color: var(--brand-blue); }
  .person-role { font-weight: 400; font-size: 21px; margin-top: 6px; }
  .contact-icons {
    position: absolute; top: 398px; left: 0; right: 0;
    display: flex; justify-content: center; gap: 5px;
  }
  .contact-icons svg { width: 19px; height: 19px; }
  .contact-lines {
    position: absolute; top: 462px; left: 0; right: 0;
    font-size: 18px; line-height: 27px;
  }
  .slogan-band { position: absolute; left: 0; right: 0; bottom: 0; height: 70px; }
  .slogan-band svg { position: absolute; inset: 0; width: 100%; height: 100%; }
  .slogan-band-text {
    position: absolute; left: 0; right: 0; bottom: 14px;
    font-weight: 600; font-size: 16.5px; letter-spacing: 0.6px; color: var(--white);
  }
  /* Back */
  .card-back { background: var(--card-black); }
  .back-lockup {
    position: absolute; top: 318px; left: 60px; right: 40px;
    display: flex; align-items: center; gap: 16px;
  }
  .back-lockup .brand-dot { width: 44px; height: 44px; }
  .back-words { display: flex; flex-direction: column; }
  .back-words .brand-name { font-size: 44px; line-height: 1; }
  .back-slogan {
    margin-top: 8px; font-weight: 600; font-size: 9.5px; letter-spacing: 1.8px;
    color: var(--brand-teal);
  }
</style>
</head>
<body>
<main class="canvas">
  <section class="card card-front" aria-label="Business card front">
    <div class="brand">
      <span class="brand-dot"></span>
      <span class="brand-name">larkfield</span>
    </div>

    <div class="person">
      <p class="person-name">John Doe</p>
      <p class="person-role">Director</p>
    </div>

    <div class="contact-icons">
      <svg viewBox="0 0 20 20" aria-label="Address">
        <circle cx="10" cy="10" r="10" fill="var(--brand-blue)"/>
        <path d="M10 4.5a3.6 3.6 0 0 0-3.6 3.6c0 2.7 3.6 7 3.6 7s3.6-4.3 3.6-7A3.6 3.6 0 0 0 10 4.5z" fill="#fff"/>
        <circle cx="10" cy="8.1" r="1.4" fill="var(--brand-blue)"/>
      </svg>
      <svg viewBox="0 0 20 20" aria-label="Phone">
        <circle cx="10" cy="10" r="10" fill="var(--brand-blue)"/>
        <path d="M7 5l2 2.2-1.2 1.4c.6 1.3 1.6 2.3 2.8 2.9l1.4-1.2L14.2 12.5 13 14.6C9.4 14.3 5.7 10.6 5.4 7z" fill="#fff"/>
      </svg>
      <svg viewBox="0 0 20 20" aria-label="Email">
        <circle cx="10" cy="10" r="10" fill="var(--brand-blue)"/>
        <rect x="5" y="6.5" width="10" height="7" rx="1" fill="#fff"/>
        <path d="M5.4 7l4.6 3.6L14.6 7" fill="none" stroke="var(--brand-blue)" stroke-width="1"/>
      </svg>
      <svg viewBox="0 0 20 20" aria-label="Website">
        <circle cx="10" cy="10" r="10" fill="var(--brand-blue)"/>
        <g fill="none" stroke="#fff" stroke-width="1">
          <circle cx="10" cy="10" r="5"/>
          <ellipse cx="10" cy="10" rx="2.2" ry="5"/>
          <path d="M5 10h10M6 7.3h8M6 12.7h8"/>
        </g>
      </svg>
    </div>

    <div class="contact-lines">
      <p>Your Address Line 1</p>
      <p>Your Address Line 2</p>
      <p>+91-11-40500000</p>
      <p>info@larkfield.com</p>
      <p>www.larkfield.com</p>
    </div>

    <div class="slogan-band">
      <svg viewBox="0 0 420 70" preserveAspectRatio="none" aria-hidden="true">
        <defs>
          <linearGradient id="bandFill" x1="0" x2="1" y1="0" y2="0">
            <stop offset="0" stop-color="#1160e6"/>
            <stop offset="0.55" stop-color="var(--brand-blue)"/>
            <stop offset="1" stop-color="var(--brand-navy)"/>
          </linearGradient>
          <linearGradient id="bandEdge" x1="0" x2="1" y1="0" y2="0">
            <stop offset="0" stop-color="#1a7fe0"/>
            <stop offset="1" stop-color="var(--brand-green)"/>
          </linearGradient>
        </defs>
        <path d="M0 26 Q190 2 420 24 L420 70 L0 70 Z" fill="url(#bandFill)"/>
        <path d="M0 26 Q190 2 420 24" fill="none" stroke="url(#bandEdge)" stroke-width="3"/>
      </svg>
      <p class="slogan-band-text">REACH YOUR FULL POTENTIAL</p>
    </div>
  </section>

  <section class="card card-back" aria-label="Business card back">
    <div class="back-lockup">
      <span class="brand-dot"></span>
      <div class="back-words">
        <span class="brand-name">larkfield</span>
        <span class="back-slogan">REACH YOUR FULL POTENTIAL</span>
      </div>
    </div>
  </section>
</main>
</body>
</html>
```